Brochure Design*

We are seeking a simple but powerful brochure design for our new company that uses electrostatic sprayers for the treatment and prevention of Covid 19 for businesses throughout the Southeast. The current brochure has too many photos and very distracting, i personally do not like anything about the brochure. Our sister company Northfield Ledger Supply was founded in 1983. Our company NLS Services LLC website is www.nlsvq.example

We need a few more days to receive feedback from our employees. Thank You

Target Market(s)

Business owners

Font styles to use
Serif
Sans Serif

Requirements
Must have
• A call for action brochure, simple while delivering a strong message
Should not have
• CLUTTER,

```html
<!DOCTYPE html>
<html lang="en">
<head>
<meta charset="utf-8">
<title>NLS Services LLC – Disinfection Flyer</title>
<link href="https://fonts.googleapis.com/css2?family=Montserrat:wght@400;500;600;700;800&display=swap" rel="stylesheet">
<style>
:root{
  --green:#5cb947;
  --dark:#474846;
  --white:#ffffff;
  --ink:#2b2b2b;
  --stage:#a9aaac;
  --teal-deep:#0f3b3f;
  --teal-mid:#3f7a7c;
  --teal-light:#a9c9c8;
}
*{margin:0;padding:0;box-sizing:border-box}
html,body{width:1200px;height:1085px;overflow:hidden}
body{background:var(--stage);font-family:"Montserrat",Arial,sans-serif;position:relative}
.page{position:absolute;top:180px;width:560px;height:725px;background:var(--white);overflow:hidden;box-shadow:0 6px 18px rgba(0,0,0,.25)}
.page--front{left:30px}
.page--back{left:610px}
.page-shapes{position:absolute;inset:0}
.brand{position:absolute;left:30px;top:32px;display:flex;align-items:center;gap:8px}
.brand-dot{width:16px;height:16px;border-radius:50%;background:var(--green)}
.brand-name{font-weight:800;font-size:20px;color:var(--green);letter-spacing:.5px}
.headline{position:absolute;right:30px;top:95px;width:340px;text-align:right;color:var(--white);font-weight:800;font-size:37px;line-height:1.08;text-transform:uppercase}
.lede{position:absolute;right:30px;top:282px;width:270px;text-align:right;color:var(--white);font-size:12.5px;line-height:1.35}
.block-title{font-weight:700;font-size:12px;text-transform:uppercase;color:var(--ink);white-space:nowrap}
.products{position:absolute;left:302px;top:452px;width:116px}
.products p{font-size:8.5px;line-height:1.3;color:var(--ink);margin-top:4px}
.product-photo{position:absolute;left:165px;top:488px;width:128px;height:88px}
.sprayers{position:absolute;left:420px;top:372px;width:125px;text-align:center}
.sprayer-photo{width:66px;height:48px;margin:6px auto 2px;border-radius:6px}
.sprayer-caption{font-size:8.5px;font-weight:600;color:var(--ink)}
.contact{position:absolute;left:30px;top:638px;color:var(--white)}
.contact h2{font-size:18px;font-weight:700;color:var(--green);margin-bottom:3px;line-height:1.1}
.contact li{list-style:none;font-size:9.5px;line-height:1.35;display:flex;gap:5px;align-items:flex-start}
.contact svg{flex:none;margin-top:2px}
.badge{position:absolute;width:60px;height:60px;border-radius:50%;background:var(--white);border:3px solid var(--green)}
.web{position:absolute;color:var(--white);font-size:10px;display:flex;gap:5px;align-items:center}
.usa-tag{position:absolute;background:var(--green);color:var(--white);font-size:8.5px;padding:3px 8px}
.tile{position:absolute;width:150px}
.tile-label{font-size:9.5px;font-weight:700;color:var(--white);text-transform:uppercase;line-height:1.15;margin-bottom:4px}
.tile-photo{width:150px;height:92px;border-radius:8px;border:2px solid var(--white)}
.germs-title{position:absolute;left:290px;top:452px;font-size:11px;font-weight:700;color:var(--ink);text-transform:uppercase;white-space:nowrap}
.germs-photo{position:absolute;left:290px;top:474px;width:98px;height:85px}
.germs-text{position:absolute;left:396px;top:472px;width:154px;font-size:7.6px;line-height:1.3;color:var(--ink)}
</style>
</head>
<body>

<section class="page page--front" aria-label="Flyer front">
  <svg class="page-shapes" width="560" height="725" viewBox="0 0 560 725">
    <defs>
      <linearGradient id="heroFill" x1="0" y1="0" x2="1" y2="1">
        <stop offset="0" stop-color="var(--teal-light)"/>
        <stop offset=".45" stop-color="var(--teal-mid)"/>
        <stop offset="1" stop-color="var(--teal-deep)"/>
      </linearGradient>
    </defs>
    <polygon points="0,150 560,20 560,320 0,575" fill="url(#heroFill)" role="img" aria-label="Photo of a technician in a protective suit spraying disinfectant over a table"/>
    <polygon points="0,140 560,10 560,22 0,152" fill="var(--green)"/>
    <polygon points="300,440 560,318 560,330 300,452" fill="var(--green)"/>
    <polygon points="0,630 560,575 560,725 0,725" fill="var(--dark)"/>
    <polygon points="0,622 560,567 560,575 0,630" fill="var(--green)"/>
  </svg>

  <div class="brand"><span class="brand-dot"></span><span class="brand-name">NLS SERVICES, LLC</span></div>

  <h1 class="headline">Protect your clients, your staff and yourself</h1>
  <p class="lede">Covid 19! NLS Services NC offers disinfection services against the coronavirus and other pathogens.</p>

  <div class="product-photo" role="img" aria-label="Photo of disinfectant jugs and a spray bottle" style="background:linear-gradient(180deg,#f2f3f3,#d6d9da)"></div>
  <div class="products">
    <h3 class="block-title">Our Products</h3>
    <p>The SurfaceShield System uses patented, EPA registered technologies to modify surfaces, providing durable long term protection that kills and inhibits the growth of bacteria, fungi, algae and viruses.</p>
  </div>

  <div class="sprayers">
    <h3 class="block-title">MistLine Sprayers</h3>
    <div class="sprayer-photo" role="img" aria-label="Photo of a cordless backpack sprayer" style="background:linear-gradient(180deg,#555,#1e1e1e)"></div>
    <div class="sprayer-caption">Cordless Backpack</div>
    <div class="sprayer-photo" role="img" aria-label="Photo of a handheld disinfectant sprayer" style="background:linear-gradient(180deg,#9a9a9a,#2a2a2a)"></div>
    <div class="sprayer-caption">Disinfectant Sprayer</div>
  </div>

  <div class="contact">
    <h2>CONTACT US</h2>
    <ul>
      <li><svg width="8" height="10" viewBox="0 0 8 10"><path d="M4 0a4 4 0 0 1 4 4c0 3-4 6-4 6S0 7 0 4a4 4 0 0 1 4-4z" fill="var(--green)"/></svg>480 Orchard Commons<br>Raleigh, North Carolina 27601</li>
      <li><svg width="9" height="9" viewBox="0 0 9 9"><path d="M1 0h2l1 2-1 1a5 5 0 0 0 3 3l1-1 2 1v2a1 1 0 0 1-1 1A8 8 0 0 1 0 1a1 1 0 0 1 1-1z" fill="var(--green)"/></svg>1-800-555-0142</li>
      <li><svg width="10" height="8" viewBox="0 0 10 8"><rect width="10" height="8" fill="var(--green)"/><path d="M0 0l5 4 5-4" stroke="var(--dark)" fill="none"/></svg>info@nlsvq.example</li>
    </ul>
  </div>
  <div class="badge" style="left:250px;top:572px"></div>
  <div class="web" style="left:250px;top:682px"><svg width="10" height="10" viewBox="0 0 10 10"><circle cx="5" cy="5" r="5" fill="var(--green)"/></svg>nlsvq.example</div>
  <div class="usa-tag" style="left:395px;top:600px">All Products Made in the USA</div>
</section>

<section class="page page--back" aria-label="Flyer back">
  <svg class="page-shapes" width="560" height="725" viewBox="0 0 560 725">
    <polygon points="0,160 560,10 560,330 0,570" fill="var(--dark)"/>
    <polygon points="0,150 560,0 560,10 0,160" fill="var(--green)"/>
    <polygon points="0,570 560,330 560,340 0,580" fill="var(--green)"/>
    <polygon points="0,630 560,590 560,725 0,725" fill="var(--dark)"/>
    <polygon points="0,622 560,582 560,590 0,630" fill="var(--green)"/>
  </svg>

  <div class="brand"><span class="brand-dot"></span><span class="brand-name">NLS SERVICES, LLC</span></div>

  <div class="tile" style="left:390px;top:50px"><div class="tile-label">Gyms<br>Sports Facilities</div><div class="tile-photo" role="img" aria-label="Photo of people training in a gym" style="background:linear-gradient(135deg,#c9c3c0,#6e5f5c)"></div></div>
  <div class="tile" style="left:210px;top:110px"><div class="tile-label">Bars<br>Restaurants</div><div class="tile-photo" role="img" aria-label="Photo of a restaurant dining room" style="background:linear-gradient(135deg,#8a6a4c,#2e2620)"></div></div>
  <div class="tile" style="left:30px;top:185px"><div class="tile-label">Offices<br>Banks</div><div class="tile-photo" role="img" aria-label="Photo of an open plan office" style="background:linear-gradient(135deg,#dcd6c4,#8d8b80)"></div></div>
  <div class="tile" style="left:390px;top:200px"><div class="tile-label">Data Centers 911<br>Call Centers</div><div class="tile-photo" role="img" aria-label="Photo of a call center operator at monitors" style="background:linear-gradient(135deg,#b89a72,#3c3a35)"></div></div>
  <div class="tile" style="left:210px;top:265px"><div class="tile-label">Schools<br>Daycares</div><div class="tile-photo" role="img" aria-label="Photo of a classroom workspace" style="background:linear-gradient(135deg,#dcd6c4,#8d8b80)"></div></div>
  <div class="tile" style="left:30px;top:345px"><div class="tile-label">Medical<br>Hospitals</div><div class="tile-photo" role="img" aria-label="Photo of a lab worker at medical screens" style="background:linear-gradient(135deg,#c7d9e6,#3b6f8e)"></div></div>

  <h3 class="germs-title">How long do germs stay on surfaces?</h3>
  <div class="germs-photo" role="img" aria-label="Illustration of a green virus particle" style="background:radial-gradient(circle at 50% 50%,#6ed04f 0,#2e8a55 35%,#3a8f98 70%,#1e5b66 100%)"></div>
  <p class="germs-text">SARS-CoV-2 can remain on surfaces for hours and up to 9 days. Research has shown that microorganisms can survive on surfaces for days, weeks, and even months, and can be hidden from current spray and wipe methods. (Lindqvist, 2006) Using electrostatic technology provides effective, proven, safe and comprehensive surface coverage and eliminates cross-contamination of dangerous pathogens.</p>

  <div class="contact">
    <h2>CONTACT US</h2>
    <ul>
      <li><svg width="8" height="10" viewBox="0 0 8 10"><path d="M4 0a4 4 0 0 1 4 4c0 3-4 6-4 6S0 7 0 4a4 4 0 0 1 4-4z" fill="var(--green)"/></svg>480 Orchard Commons<br>Raleigh, North Carolina 27601</li>
      <li><svg width="9" height="9" viewBox="0 0 9 9"><path d="M1 0h2l1 2-1 1a5 5 0 0 0 3 3l1-1 2 1v2a1 1 0 0 1-1 1A8 8 0 0 1 0 1a1 1 0 0 1 1-1z" fill="var(--green)"/></svg>1-800-555-0142</li>
      <li><svg width="10" height="8" viewBox="0 0 10 8"><rect width="10" height="8" fill="var(--green)"/><path d="M0 0l5 4 5-4" stroke="var(--dark)" fill="none"/></svg>info@nlsvq.example</li>
    </ul>
  </div>
  <div class="badge" style="left:250px;top:580px"></div>
  <div class="web" style="left:250px;top:686px"><svg width="10" height="10" viewBox="0 0 10 10"><circle cx="5" cy="5" r="5" fill="var(--green)"/></svg>nlsvq.example</div>
  <div class="usa-tag" style="left:395px;top:606px">All Products Made in the USA</div>
</section>

</body>
</html>
```